Sunset Harbour Living Web Page

We need a web page design that has two intro pages - first being a 'home page', then a link to the second page that has the 'content tabs' and a 'call to action' (see below).

The business helps people that wish to retire to S.E.Asia (Thailand, Malaysia, Indonesia,The Philippines etc) - to enjoy the lifestyle and the remaining years of their lives. What attracts S.E.Asia to many people is the lower cost, the atmoshpere and beauty of the tropics and the vibrancy of the various countries.

People that are wishing to make the most of their retirement and are adventurous at a great bargain compared to the cost of their own countries will be interested.

We help them achieve this - visa, financials (tax, gov't payments etc), introduce them to the right people for property, clubs, retirement facilities, insurance and so forth.

Therefore we are providing an extremely wide ranging service and this site will provide broad but general information only - with a call to action to come and see us for more specific information and how we can help them specifically.

This site will be predominantly for travel and lifestyle, it will be linked with another financial services (financial planning) site later down the track.

The colour scheme is dark green and blue - as per the attached logo design. Photos and background just think lifestyle and S.E.Asia - beaches/mountains/water/recreational activities for retirees.

Target market is mostly those coming up to retirement to those that are already retired. But we also expect to have some interest with younger people that would like to find out more and plan for the future. So a broad age group but I would say mostly 40-70 yrs old.

On the first (Home) page we would like our company name 'Sunset Harbour Living', our logo (which will be on all pages) and a statement such as: “Imagine a retirement where your dreams are brought to life, and you have never felt more alive. Let us show you how”. Then a link to the second page.

We would like an uncluttered site. On the second (contents) page the tabs would be:

- Visa
- Property
- Financials
- Travel
- Insurance & Healthcare
- Medical Tourism
- Cost of living
- Weekly Blogs and articles
- Sunset Harbour Living story

We would also like a call to action on the second page - asking them to leave their contact details if they wish to learn more or sign up to our weekly newsletter/blog.

We are open to suggestions and your imaginations.

Thank you
Gerald

Font styles to use
Serif
Script

Colors
0255a3
3377b5
00a990
9bcb3c
abd036
33b8a4
85abd2
cadf82
86cfc6

Requirements
Must have
• I have been asked by the web designer to receive a 'Web Font' so that we can 'get off of Plixora'. Hope that makes sense.

```html
<!DOCTYPE html>
<html lang="en">
<head>
<meta charset="utf-8">
<title>Sunset Harbour Living</title>
<link rel="stylesheet" href="https://fonts.googleapis.com/css2?family=Roboto+Condensed:wght@300;400;700&family=Roboto:wght@300;400;500&display=swap">
<style>
:root{
  --blue-deep:#0255a3;
  --blue-mid:#3377b5;
  --blue-nav:#1a9fe0;
  --blue-nav-dark:#0a78c4;
  --teal:#00a990;
  --teal-soft:#86cfc6;
  --green:#16a05a;
  --lime:#9bcb3c;
  --lime-dark:#7aa82a;
  --sky-soft:#85abd2;
  --lime-soft:#cadf82;
  --ink:#3a3a3a;
  --muted:#8a8a8a;
  --footer:#1f1f1f;
  --white:#ffffff;
}
*{box-sizing:border-box;margin:0;padding:0}
html,body{width:1200px;height:2616px;overflow:hidden;background:var(--white)}
body{font-family:"Roboto",Arial,sans-serif;color:var(--ink);position:relative}
.abs{position:absolute}

/* header */
.topline{left:0;top:0;width:1200px;height:4px;background:var(--green)}
.brand{left:99px;top:28px;display:flex;align-items:center;gap:10px}
.brand-dot{width:34px;height:34px;border-radius:50%;background:var(--teal)}
.brand-name{font-family:"Roboto Condensed",sans-serif;font-weight:700;font-size:22px;color:var(--blue-deep)}
.contact{display:flex;align-items:center;gap:14px;top:28px}
.contact-icon{width:44px;height:44px;border-radius:50%;background:var(--lime);border:3px solid #dcebb8;display:flex;align-items:center;justify-content:center}
.contact-text{font-size:12.5px;color:#666;line-height:21px}
.nav{left:0;top:101px;width:1200px;height:59px;background:linear-gradient(var(--blue-nav),var(--blue-nav-dark));display:flex;align-items:center;padding-left:99px}
.nav a{color:var(--white);text-decoration:none;font-family:"Roboto Condensed",sans-serif;font-size:13px;margin-right:20px}

/* hero */
.hero{left:0;top:160px;width:1200px;height:463px;
  background:
    radial-gradient(ellipse 420px 160px at 820px 120px,rgba(30,24,20,.75),transparent 70%),
    radial-gradient(ellipse 520px 220px at 300px 380px,rgba(120,95,60,.55),transparent 70%),
    linear-gradient(180deg,#a49a8e 0%,#6e6254 28%,#4a3e31 55%,#2a221b 80%,#1a1511 100%)}
.hero-title{left:0;width:1200px;top:290px;text-align:center;color:var(--white);font-family:"Roboto Condensed",sans-serif;font-weight:700;font-size:34px;line-height:51px;letter-spacing:.6px;text-shadow:0 1px 3px rgba(0,0,0,.4)}
.btn-ghost{border:2px solid var(--white);border-radius:26px;color:var(--white);display:flex;align-items:center;justify-content:center;font-family:"Roboto Condensed",sans-serif}
.hero-btn{left:455px;top:434px;width:272px;height:47px;font-size:23px}
.hero-arrow{top:375px;width:40px;height:40px;border-radius:50%;border:2px solid rgba(255,255,255,.6);background:rgba(0,0,0,.3);display:flex;align-items:center;justify-content:center}

/* welcome */
.welcome{left:0;top:623px;width:1200px;height:280px;background:var(--teal)}
.welcome-title{left:0;width:1200px;top:664px;text-align:center;color:var(--white);font-family:"Roboto Condensed",sans-serif;font-size:31px;font-weight:400}
.welcome-text{left:227px;width:746px;top:720px;text-align:center;color:var(--white);font-size:11.5px;line-height:19px}
.pill{display:flex;align-items:center;justify-content:space-between;border-radius:24px;padding-left:22px}
.pill-arrow{border-radius:50%;display:flex;align-items:center;justify-content:center}
.welcome-btn{left:522px;top:809px;width:155px;height:42px;border:2px solid var(--white);color:var(--white);font-family:"Roboto Condensed",sans-serif;font-size:15px;padding-right:2px}
.welcome-btn .pill-arrow{width:38px;height:38px;background:var(--white)}
.notch{left:582px;top:903px;width:0;height:0;border-left:18px solid transparent;border-right:18px solid transparent;border-top:18px solid var(--teal)}

/* service cards */
.card{top:957px;width:318px;height:421px;background:#f7f7f7;border:4px solid #ececec}
.card-photo{position:absolute;left:13px;top:13px;width:284px;height:162px}
.card-title{position:absolute;left:0;width:100%;top:208px;text-align:center;font-size:21px;font-weight:300;letter-spacing:.5px;color:#333}
.card-text{position:absolute;left:22px;width:266px;top:244px;text-align:center;font-size:11px;line-height:20px;color:var(--muted);hyphens:auto}
.card-btn{position:absolute;left:97px;top:344px;width:116px;height:38px;border:2px solid var(--green);color:var(--green);font-size:11.5px;padding-left:12px;padding-right:2px}
.card-btn .pill-arrow{width:32px;height:32px;background:var(--green)}

/* travel */
.travel-photo{left:0;top:1430px;width:603px;height:427px;
  background:
    radial-gradient(ellipse 260px 140px at 470px 60px,rgba(200,225,215,.8),transparent 70%),
    radial-gradient(ellipse 200px 240px at 200px 220px,rgba(110,70,55,.85),transparent 70%),
    radial-gradient(ellipse 360px 140px at 300px 400px,rgba(70,110,40,.9),transparent 70%),
    linear-gradient(160deg,#9fc0ae 0%,#6f7f5a 35%,#5e4a3a 60%,#3e5a2a 100%)}
.travel-panel{left:603px;top:1430px;width:597px;height:427px;background:linear-gradient(135deg,var(--blue-deep) 0%,#0a5fb0 60%,var(--blue-deep) 100%)}
.travel-title{left:647px;top:1462px;color:var(--white);font-family:"Roboto Condensed",sans-serif;font-size:25px;font-weight:400}
.travel-sub{left:651px;top:1503px;color:var(--white);font-family:"Roboto Condensed",sans-serif;font-size:15px}
.travel-text{left:653px;width:448px;color:#dfe8f3;font-size:11.5px;line-height:20px;text-align:justify;hyphens:auto}
.travel-btn{left:652px;top:1768px;width:155px;height:41px;border:2px solid var(--white);color:var(--white);font-family:"Roboto Condensed",sans-serif;font-size:16px;padding-right:2px}
.travel-btn .pill-arrow{width:35px;height:35px;border:2px solid var(--white)}
.slide-ctrl{top:1460px;width:22px;height:22px;border-radius:50%;background:rgba(255,255,255,.35);border:1px solid rgba(255,255,255,.7);display:flex;align-items:center;justify-content:center}

/* insurance */
.insurance{left:0;top:1857px;width:1200px;height:396px;background:#f4f4f4}
.insurance-title{left:0;width:1200px;top:1900px;text-align:center;font-family:"Roboto Condensed",sans-serif;font-size:31px;color:#444;font-weight:400}
.feature{top:1978px;width:314px;text-align:center}
.feature-icon{width:90px;height:90px;border-radius:50%;border:3px solid #fff;box-shadow:0 0 0 2px #ddd;margin:0 auto;display:flex;align-items:center;justify-content:center}
.feature-title{margin-top:30px;font-size:17px;color:#333;letter-spacing:.3px;font-weight:400}
.feature-text{margin:8px auto 0;width:284px;font-size:11.5px;line-height:21px;color:var(--muted)}

/* newsletter */
.newsletter{left:197px;top:2215px;width:806px;height:73px;background:var(--lime);z-index:2}
.newsletter-label{position:absolute;left:59px;top:23px;color:var(--white);font-family:"Roboto Condensed",sans-serif;font-size:22px}
.newsletter-field{position:absolute;left:358px;top:16px;width:362px;height:42px;border:1px solid rgba(255,255,255,.8);border-radius:22px}
.newsletter-send{position:absolute;right:3px;top:3px;width:120px;height:34px;border-radius:18px;background:var(--lime-dark);color:var(--white);font-size:16px;display:flex;align-items:center;justify-content:center}

/* footer */
.footer{left:0;top:2253px;width:1200px;height:293px;background:var(--footer)}
.footer-brand{left:140px;top:2395px;display:flex;align-items:center;gap:12px}
.footer-brand .brand-dot{width:48px;height:48px;background:var(--white)}
.footer-brand .brand-name{color:var(--white);font-size:25px;white-space:nowrap}
.footer-heading{top:2331px;color:var(--white);font-size:16px;letter-spacing:.5px;font-weight:400}
.footer-info{left:485px;top:2374px;color:#8f8f8f;font-size:11.5px;line-height:20px;width:260px}
.footer-info p{margin-bottom:9px}
.footer-links{top:2375px;list-style:none;color:#8f8f8f;font-size:11.5px}
.footer-links li{height:30px}
.footer-links li::before{content:"›";margin-right:12px;color:#777}
.bottombar{left:0;top:2546px;width:1200px;height:70px;background:linear-gradient(var(--blue-nav),var(--blue-nav-dark))}
.social{top:2567px;width:27px;height:27px;border-radius:50%;border:1.5px solid var(--white);display:flex;align-items:center;justify-content:center}
.copyright{left:780px;top:2573px;color:var(--white);font-size:13px}
</style>
</head>
<body>

<div class="abs topline"></div>
<div class="abs brand"><span class="brand-dot"></span><span class="brand-name">Sunset Harbour Living</span></div>

<div class="abs contact" style="left:690px">
  <span class="contact-icon"><svg width="20" height="20" viewBox="0 0 24 24"><path d="M6.6 10.8a15 15 0 0 0 6.6 6.6l2.2-2.2c.3-.3.7-.4 1-.2 1.1.4 2.3.6 3.6.6.6 0 1 .4 1 1V20c0 .6-.4 1-1 1A17 17 0 0 1 3 4c0-.6.4-1 1-1h3.5c.6 0 1 .4 1 1 0 1.3.2 2.5.6 3.6.1.3 0 .7-.2 1z" fill="#fff"/></svg></span>
  <div class="contact-text">CALL US ON :<br>(055) - 4127730916</div>
</div>
<div class="abs contact" style="left:900px">
  <span class="contact-icon"><svg width="20" height="20" viewBox="0 0 24 24"><rect x="3" y="5" width="18" height="14" rx="2" fill="none" stroke="#fff" stroke-width="2"/><path d="M3 7l9 6 9-6" fill="none" stroke="#fff" stroke-width="2"/></svg></span>
  <div class="contact-text">MAIL US ON :<br>info@sunsetharbourliving.com</div>
</div>

<nav class="abs nav">
  <a>Home</a><a>Visa</a><a>Property</a><a>Financials</a><a>Travel</a><a>Insurance &amp; Healthcare</a><a>Medical Tourism</a><a>Cost of living</a><a>Weekly Blogs and articles</a><a>Sunset Harbour Living story</a><a style="margin-right:0">Contact us</a>
</nav>

<div class="abs hero" role="img" aria-label="Photo of misty mountain ridges at dusk"></div>
<div class="abs hero-title">IMAGINE A RETIREMENT WHERE YOUR DREAMS ARE<br>BROUGHT TO LIFE, AND YOU HAVE NEVER FELT MORE ALIVE</div>
<div class="abs btn-ghost hero-btn">Let us show you how</div>
<div class="abs hero-arrow" style="left:29px"><svg width="14" height="14" viewBox="0 0 14 14"><path d="M10 1L3 7l7 6z" fill="#fff"/></svg></div>
<div class="abs hero-arrow" style="left:1125px"><svg width="14" height="14" viewBox="0 0 14 14"><path d="M4 1l7 6-7 6z" fill="#fff"/></svg></div>

<section class="abs welcome"></section>
<h1 class="abs welcome-title">WELCOME TO SUNSET HARBOUR LIVING</h1>
<p class="abs welcome-text">It is a long established fact that a reader will be distracted by the readable content of a page when looking at its layout. The point of using Lorem Ipsum is that it has a more-or-less normal distribution of letters, as opposed to using 'Content here, content here', making it look like readable English. Many desktop publishing packages and web page editors now use Lorem Ipsum as their default model</p>
<div class="abs pill welcome-btn">Learn More<span class="pill-arrow"><svg width="14" height="12" viewBox="0 0 14 12"><path d="M2 2l4 4-4 4M7 2l4 4-4 4" fill="none" stroke="#00a990" stroke-width="2"/></svg></span></div>
<div class="abs notch"></div>

<article class="abs card" style="left:99px">
  <div class="card-photo" role="img" aria-label="Photo of lanterns rising over a temple at night" style="background:radial-gradient(ellipse 80px 60px at 150px 120px,rgba(230,150,60,.8),transparent 70%),radial-gradient(ellipse 60px 40px at 240px 130px,rgba(220,90,40,.7),transparent 70%),linear-gradient(180deg,#0b1322 0%,#1b1d2a 50%,#3a2a1a 80%,#6b3f1e)"></div>
  <h2 class="card-title">VISA</h2>
  <p class="card-text">There are many variations of passages of Lorem Ipsum available, but the majority have suffered alteration in some form, by injected humour, or randomised words which don't look even slightly</p>
  <div class="pill card-btn">Learn More<span class="pill-arrow"><svg width="12" height="10" viewBox="0 0 14 12"><path d="M2 2l4 4-4 4M7 2l4 4-4 4" fill="none" stroke="#fff" stroke-width="2"/></svg></span></div>
</article>
<article class="abs card" style="left:441px">
  <div class="card-photo" role="img" aria-label="Photo of a countryside ride through green fields" style="background:radial-gradient(ellipse 70px 50px at 230px 80px,rgba(60,120,40,.8),transparent 70%),linear-gradient(180deg,#5aa7e6 0%,#b9dcf2 42%,#7fb04c 55%,#4e8a2e 78%,#3b6d22)"></div>
  <h2 class="card-title">PROPERTY</h2>
  <p class="card-text">There are many variations of passages of Lorem Ipsum available, but the majority have suffered alteration in some form, by injected humour, or randomised words which don't look even slightly</p>
  <div class="pill card-btn">Learn More<span class="pill-arrow"><svg width="12" height="10" viewBox="0 0 14 12"><path d="M2 2l4 4-4 4M7 2l4 4-4 4" fill="none" stroke="#fff" stroke-width="2"/></svg></span></div>
</article>
<article class="abs card" style="left:783px">
  <div class="card-photo" role="img" aria-label="Photo of hilltop pagodas under a blue sky" style="background:radial-gradient(ellipse 70px 60px at 90px 100px,rgba(225,180,160,.85),transparent 70%),linear-gradient(180deg,#3f86d2 0%,#9cc2e8 45%,#c7a898 65%,#7a8a5a 82%,#4f7a44)"></div>
  <h2 class="card-title">FINANCIALS</h2>
  <p class="card-text">There are many variations of passages of Lorem Ipsum available, but the majority have suffered alteration in some form, by injected humour, or randomised words which don't look even slightly</p>
  <div class="pill card-btn">Learn More<span class="pill-arrow"><svg width="12" height="10" viewBox="0 0 14 12"><path d="M2 2l4 4-4 4M7 2l4 4-4 4" fill="none" stroke="#fff" stroke-width="2"/></svg></span></div>
</article>

<div class="abs travel-photo" role="img" aria-label="Photo of a tiered temple surrounded by tropical forest"></div>
<div class="abs slide-ctrl" style="left:516px"><svg width="8" height="8" viewBox="0 0 8 8"><path d="M6 0L1 4l5 4z" fill="#fff"/></svg></div>
<div class="abs slide-ctrl" style="left:544px"><svg width="8" height="8" viewBox="0 0 8 8"><path d="M2 0l5 4-5 4z" fill="#fff"/></svg></div>
<section class="abs travel-panel"></section>
<h2 class="abs travel-title">Travel to Malaysia</h2>
<p class="abs travel-sub">To Enjoy The Lifestyle And The Remaining Years Of Their Lives.</p>
<p class="abs travel-text" style="top:1544px">Sed ut perspiciatis unde omnis iste natus error sit voluptatem accusantium doloremque laudantium, totam rem aperiam, eaque ipsa quae ab illo inventore veritatis et quasi architecto beatae vitae dicta sunt explicabo. Nemo enim ipsam voluptatem quia voluptas sit aspernatur aut odit aut fugit, sed quia consequuntur magni dolores eos qui ratione voluptatem sequi nesciunt.</p>
<p class="abs travel-text" style="top:1672px">Neque porro quisquam est, qui dolorem ipsum quia dolor sit amet, consectetur, adipisci velit, sed quia non numquam eius modi tempora incidunt ut labore et dolore magnam aliquam quaerat voluptatem.</p>
<div class="abs pill travel-btn">Learn More<span class="pill-arrow"><svg width="12" height="10" viewBox="0 0 14 12"><path d="M2 2l4 4-4 4M7 2l4 4-4 4" fill="none" stroke="#fff" stroke-width="2"/></svg></span></div>

<section class="abs insurance"></section>
<h2 class="abs insurance-title">INSURANCE &amp; HEALTHCARE</h2>
<div class="abs feature" style="left:82px">
  <div class="feature-icon" style="background:var(--teal-soft)"><svg width="40" height="40" viewBox="0 0 40 40"><circle cx="20" cy="20" r="14" fill="none" stroke="#fff" stroke-width="2.5"/><path d="M27 13l-4 10-10 4 4-10z" fill="none" stroke="#fff" stroke-width="2"/></svg></div>
  <h3 class="feature-title">FINIBUS BONORUM</h3>
  <p class="feature-text">Sed ut perspiciatis unde omnis iste natus error sit voluptatem accusantium doloremque laudantium, totam rem aperiam, eaque ipsa quae</p>
</div>
<div class="abs feature" style="left:443px">
  <div class="feature-icon" style="background:var(--sky-soft)"><svg width="40" height="40" viewBox="0 0 40 40"><circle cx="28" cy="12" r="5" fill="#fff"/><path d="M6 32h28" stroke="#fff" stroke-width="3"/><path d="M10 28c4-3 8-3 12 0" fill="none" stroke="#fff" stroke-width="2.5"/></svg></div>
  <h3 class="feature-title">FINIBUS BONORUM</h3>
  <p class="feature-text">Sed ut perspiciatis unde omnis iste natus error sit voluptatem accusantium doloremque laudantium, totam rem aperiam, eaque ipsa quae</p>
</div>
<div class="abs feature" style="left:804px">
  <div class="feature-icon" style="background:var(--lime-soft)"><svg width="40" height="40" viewBox="0 0 40 40"><rect x="6" y="12" width="28" height="20" rx="3" fill="#fff"/><rect x="14" y="8" width="10" height="5" fill="#fff"/><circle cx="20" cy="22" r="6" fill="#cadf82"/></svg></div>
  <h3 class="feature-title">FINIBUS BONORUM</h3>
  <p class="feature-text">Sed ut perspiciatis unde omnis iste natus error sit voluptatem accusantium doloremque laudantium, totam rem aperiam, eaque ipsa quae</p>
</div>

<div class="abs newsletter">
  <span class="newsletter-label">NEWSLETTER SIGN UP</span>
  <div class="newsletter-field"><span class="newsletter-send">SEND NOW</span></div>
</div>

<footer class="abs footer"></footer>
<div class="abs brand footer-brand"><span class="brand-dot"></span><span class="brand-name">Sunset Harbour Living</span></div>
<h4 class="abs footer-heading" style="left:485px">GET IN TOUCH</h4>
<div class="abs footer-info">
  <p>Address : 200 Latin words, combined with a handful of model sentence structures</p>
  <p>Phone No : (055) - 412773091</p>
  <p>Mail Id : info@sunsetharbourliving.com</p>
  <p>Fax : (005) - 4127730916</p>
</div>
<h4 class="abs footer-heading" style="left:830px">INFORMATION</h4>
<ul class="abs footer-links" style="left:830px">
  <li>Home</li><li>Visa</li><li>Property</li><li>Financials</li><li>Travel</li>
</ul>
<ul class="abs footer-links" style="left:952px">
  <li>Insurance &amp; Healthcare</li><li>Medical Tourism</li><li>Cost of living</li><li>Weekly Blogs and articles</li><li>Sunset Harbour Living story</li>
</ul>

<div class="abs bottombar"></div>
<span class="abs social" style="left:100px"><svg width="13" height="13" viewBox="0 0 24 24"><path d="M4 5h16v11H9l-5 4z" fill="#fff"/></svg></span>
<span class="abs social" style="left:139px"><svg width="13" height="13" viewBox="0 0 24 24"><rect x="3" y="6" width="18" height="12" rx="1.5" fill="none" stroke="#fff" stroke-width="2.2"/><path d="M3 7l9 6 9-6" fill="none" stroke="#fff" stroke-width="2"/></svg></span>
<span class="abs social" style="left:177px"><svg width="13" height="13" viewBox="0 0 24 24"><path d="M12 2a7 7 0 0 0-7 7c0 5 7 13 7 13s7-8 7-13a7 7 0 0 0-7-7z" fill="#fff"/><circle cx="12" cy="9" r="2.6" fill="#1a8fd6"/></svg></span>
<p class="abs copyright">Copyrights@2016Company Name All rights reserved</p>

</body>
</html>
```